Financial Planning firm focused on serving women 55-65 yrs old needs stationary design

We are rebranding our financial planning firm and our target client is a 55-65 yr old women. We need a stationary design to go with our new logo.

Contact Information: Raymond Kessler, MS, CFP President Harlow Wealth Management 4820 Bramblewood Lane, Suite 317 Estero, FL 33961 ray@harlowwealthmgmt.example phone 239-555-0184

```html
<!DOCTYPE html>
<html lang="en">
<head>
<meta charset="utf-8">
<title>Harlow Wealth Management – Business Card</title>
<link rel="stylesheet" href="https://fonts.googleapis.com/css2?family=Open+Sans:wght@400;600;700&display=swap">
<style>
  :root{
    --page:#e9e6e1;
    --card-white:#ffffff;
    --brand-blue:#2f5c8c;
    --brand-green:#1f6b3a;
    --leaf-green:#236b3c;
    --sage:#a9b8ac;
    --ink:#333333;
    --deep-green:#0f4a2b;
    --mid-green:#1b6e3f;
    --bright-green:#2ea55a;
    --white:#ffffff;
  }
  *{box-sizing:border-box;margin:0;padding:0}
  html,body{width:1200px;height:771px;overflow:hidden}
  body{background:var(--page);font-family:"Open Sans",Arial,sans-serif;position:relative}

  .card{position:absolute;width:600px;height:341px;overflow:hidden}
  .card--front{left:132px;top:22px;background:var(--card-white);border-radius:22px;box-shadow:0 4px 14px rgba(0,0,0,.18)}
  .card--back{left:462px;top:398px;background:linear-gradient(135deg,var(--mid-green),var(--deep-green));box-shadow:0 4px 14px rgba(0,0,0,.25)}

  .brand{position:absolute;display:flex;align-items:center;gap:20px}
  .brand__dot{border-radius:50%;flex:none}
  .brand__name{font-weight:600;line-height:1;letter-spacing:1px}
  .brand__name .line1{display:block;font-size:44px}
  .brand__name .line2{display:block;font-size:12px;letter-spacing:1.2px;margin-top:8px}

  .card--front .brand{left:37px;top:30px}
  .card--front .brand__dot{width:92px;height:92px;background:var(--sage)}
  .card--front .brand__name{color:var(--brand-blue)}

  .contact{position:absolute;left:36px;top:158px;font-size:13px;color:var(--ink);line-height:19px}
  .contact__row{display:flex;align-items:center;gap:6px}
  .contact__row svg{width:11px;height:11px;flex:none}
  .contact__address{margin-top:26px;line-height:21px}

  .tree-art{position:absolute;left:372px;top:112px;width:156px;height:160px;border-radius:48% 52% 30% 30%;background:radial-gradient(circle at 50% 40%,#2c7c48,var(--leaf-green))}

  .swoosh{position:absolute;left:0;bottom:0;width:600px;height:80px}
  .signature{position:absolute;right:24px;bottom:18px;color:var(--white);font-size:11px}
  .signature strong{font-size:17px;font-weight:700;margin-right:4px}

  .back-circle{position:absolute;left:-271px;top:-79px;width:502px;height:502px;border-radius:50%;background:radial-gradient(circle at 70% 50%,var(--bright-green),#1e8646)}
  .card--back .brand{left:262px;top:117px}
  .card--back .brand__dot{width:102px;height:102px;background:var(--white)}
  .card--back .brand__name{color:var(--white)}
</style>
</head>
<body>

<section class="card card--front" aria-label="Business card front">
  <div class="brand">
    <span class="brand__dot"></span>
    <span class="brand__name"><span class="line1">HARLOW</span><span class="line2">WEALTH MANAGEMENT</span></span>
  </div>

  <div class="contact">
    <div class="contact__row">
      <svg viewBox="0 0 12 12"><path d="M3 1l2 2-1 1.5c.6 1.3 1.5 2.2 2.8 2.8L8.3 6l2 2-1.2 1.8C5.5 9.5 2.5 6.5 1.2 2.2z" fill="var(--ink)"/></svg>
      <span>239-555-0184</span>
    </div>
    <div class="contact__row">
      <svg viewBox="0 0 12 12"><rect x="1" y="3" width="10" height="7" fill="var(--ink)"/><path d="M1 3l5 4 5-4" stroke="#fff" fill="none"/></svg>
      <span>ray@harlowwealthmgmt.example</span>
    </div>
    <div class="contact__address">4820 Bramblewood Lane,<br>Suite 317 Estero, FL 33961</div>
  </div>

  <div class="tree-art" role="img" aria-label="Green tree illustration"></div>

  <svg class="swoosh" viewBox="0 0 600 80" preserveAspectRatio="none">
    <path d="M0 66 C180 40 400 20 600 14 L600 80 L0 80Z" fill="var(--brand-green)"/>
    <path d="M0 62 C180 34 400 16 600 9" stroke="var(--white)" stroke-width="5" fill="none"/>
    <path d="M0 58 C180 30 400 12 600 4" stroke="var(--brand-blue)" stroke-width="3" fill="none"/>
  </svg>
  <div class="signature"><strong>Raymond Kessler</strong>MS, CFP President</div>
</section>

<section class="card card--back" aria-label="Business card back">
  <div class="back-circle"></div>
  <div class="brand">
    <span class="brand__dot"></span>
    <span class="brand__name"><span class="line1">HARLOW</span><span class="line2">WEALTH MANAGEMENT</span></span>
  </div>
</section>

</body>
</html>
```